BrightNomadRx.com Blog Design (Travel, Lifestyle, and Life Hacking blog)

I am launching a lifestyle blog about my life. I'm a doctor who travels the world trying the best restaurants, airlines and trying to have as much fun as possible. I also invest in startups, and am always trying new tricks to make life better. I also plan to write about various other topics, but essentially it is about travel, lifestyle and medicine. I need a creative and really awesome looking design for a new wordpress blog called BrightNomadRx

Target Market(s)

Physicians, Entrepreneurs, Travellers

Industry/Entity Type

Airlines

Number of Pages Required

1 page

Font styles to use
Serif

Requirements
Must have
• Slick looking graphics with a highly professional modern feel

```html
<!DOCTYPE html>
<html lang="en">
<head>
<meta charset="utf-8">
<title>BrightNomadRx.com – Travel, Lifestyle &amp; Medicine Blog</title>
<link href="https://fonts.googleapis.com/css2?family=Libre+Baskerville:wght@700&family=Oswald:wght@400;500&family=Open+Sans:wght@400;700&family=Josefin+Sans:wght@400;600&family=Roboto+Condensed:wght@700&display=swap" rel="stylesheet">
<style>
:root{
  --cyan:#2bb5d8;
  --red:#f0483a;
  --orange:#f7931e;
  --btn-orange:#f26a2a;
  --green:#4caf3f;
  --ink:#222;
  --text:#333;
  --muted:#8a8a8a;
  --panel:#eeeeee;
  --dark:#2a2a2a;
  --darker:#1b1b1b;
  --white:#fff;
  --fb:#3b5a99;
  --tw:#3fb2e6;
  --yt:#cf2a2a;
  --vm:#2aa8dc;
  --dr:#e85b95;
  --rss:#f58a2b;
}
*{box-sizing:border-box;margin:0;padding:0}
html,body{width:1200px;height:3991px;overflow:hidden}
body{position:relative;background:var(--white);font-family:"Josefin Sans",sans-serif;color:var(--text)}
.abs{position:absolute}

/* top bar */
.topbar{left:0;top:0;width:1200px;height:58px;background:var(--darker)}
.logo{left:72px;top:12px;font:700 30px/34px "Libre Baskerville",serif;color:var(--white)}
.social-top{right:75px;top:17px;display:flex;gap:5px}
.ico{width:24px;height:24px;border:1.5px solid #888;border-radius:50%;display:block}
.navbar{left:0;top:58px;width:1200px;height:48px;background:#2e2e2e}
.nav{left:72px;top:0;display:flex;height:48px}
.nav a{font:400 15px/48px "Oswald",sans-serif;color:var(--white);text-decoration:none;padding:0 13px;text-transform:uppercase}
.nav a.active{background:var(--red)}
.search{right:75px;top:9px;width:293px;height:31px;background:#555;color:#ccc;font:400 13px/31px "Open Sans",sans-serif;padding-left:12px}
.search svg{position:absolute;right:10px;top:8px}

/* hero */
.hero{left:0;top:106px;width:1200px;height:559px;background:linear-gradient(120deg,#f6c35a 0%,#d49a44 25%,#7c8a3f 55%,#4a5a2a 80%,#2e3a1e 100%)}
.hero-tag{left:72px;top:314px;background:var(--red);color:var(--white);font:400 14px/26px "Oswald",sans-serif;padding:0 12px}
.hero-title{left:72px;top:352px;width:680px;font:700 25px/33px "Roboto Condensed",sans-serif;color:var(--white);text-shadow:0 1px 4px rgba(0,0,0,.5)}

/* section heads */
.sec-head{height:32px;border-bottom:3px solid var(--cyan)}
.sec-head .tab{display:inline-block;background:var(--cyan);color:var(--white);font:400 16px/32px "Oswald",sans-serif;padding:0 12px;text-transform:uppercase}
.sec-head .more{position:absolute;right:0;top:7px;background:var(--ink);color:var(--white);font:500 11px/18px "Oswald",sans-serif;padding:0 8px}
.sec-head.red{border-color:var(--red)}.sec-head.red .tab{background:var(--red)}
.sec-head.orange{border-color:var(--orange)}.sec-head.orange .tab{background:var(--orange)}

/* photo placeholders */
.ph{display:block}
.ph-sea{background:linear-gradient(180deg,#8ec3e6,#4f8fb8 55%,#3c6a4a)}
.ph-beach{background:linear-gradient(160deg,#a9dcef,#5fb5cf 50%,#d9c59a)}
.ph-boat{background:linear-gradient(180deg,#7fc3e2,#2f86a8 60%,#c9a36b)}
.ph-girl{background:linear-gradient(150deg,#e9d3a8,#b58c5d 55%,#6a7a4c)}
.ph-people{background:linear-gradient(140deg,#d7a36b,#8a5c3e 55%,#5a7aa4)}
.ph-pills{background:linear-gradient(150deg,#e3e8ec,#8ab1c8 45%,#c24d4a 80%)}
.ph-doctor{background:linear-gradient(150deg,#f2f4f6,#c9d6de 60%,#9bb1bf)}
.ph-food{background:linear-gradient(150deg,#f3f1ea,#9dbb5a 55%,#4e7a2e)}
.ph-car{background:linear-gradient(160deg,#f4c77d,#b9804a 55%,#3c3b38)}
.ph-laptop{background:linear-gradient(160deg,#1a2a3a,#2f6b8f 55%,#0f1418)}
.ph-bike{background:linear-gradient(160deg,#dbe8ef,#9fbfd1 55%,#5c7a8c)}
.ph-watch{background:linear-gradient(160deg,#f4efe8,#b54a3a 45%,#5a2a22)}

/* feature card */
.feature{position:relative;height:295px;overflow:hidden}
.feature .ph{position:absolute;inset:0}
.feature .shade{position:absolute;left:0;right:0;bottom:0;height:150px;background:linear-gradient(180deg,rgba(0,0,0,0),rgba(0,0,0,.65))}
.feature .cap{position:absolute;left:20px;right:20px;bottom:22px;text-align:center;color:var(--white)}
.badge{display:inline-block;background:var(--green);color:var(--white);font:600 9px/15px "Open Sans",sans-serif;padding:0 7px;text-transform:uppercase}
.feature h3{font:700 17px/22px "Open Sans",sans-serif;margin:8px 0 6px}
.feature .meta{color:#ddd}

.meta{font:400 9.5px/14px "Open Sans",sans-serif;color:var(--muted)}
.meta span{margin-right:10px}

/* small post item */
.mini{display:flex;gap:11px;height:104px}
.mini .ph{width:125px;height:88px;flex:none}
.mini h4{font:700 13px/17px "Open Sans",sans-serif;color:var(--ink);margin:2px 0 4px}

/* layout columns */
.col-main{left:72px;width:708px}
.col-side{left:793px;width:332px}
.two{display:flex;gap:12px}
.two>div{width:348px;position:relative}

/* recent posts */
.post{display:flex;gap:16px;height:176px}
.post .thumb{position:relative;width:231px;height:155px;flex:none}
.post .thumb .ph{position:absolute;inset:0}
.cat{position:absolute;left:6px;top:8px;color:var(--white);font:600 10px/18px "Open Sans",sans-serif;padding:0 8px;text-transform:uppercase}
.post h4{font:700 15px/20px "Open Sans",sans-serif;color:var(--ink);margin-top:4px}
.post .meta{margin:8px 0 6px}
.post p{font:400 13px/18px "Josefin Sans",sans-serif;color:#555}
.btn-read{display:inline-block;margin-top:10px;background:var(--btn-orange);color:var(--white);font:600 10px/22px "Open Sans",sans-serif;padding:0 12px}
.pager{font:600 13px/20px "Open Sans",sans-serif;color:var(--ink)}
.pager span{color:var(--muted);margin:0 12px}

/* sidebar */
.about{background:#363636;height:420px;text-align:center;color:#ddd;padding:31px 28px 0}
.avatar{width:124px;height:124px;border-radius:50%;margin:0 auto;background:radial-gradient(circle,#7b8a96,#3a4650);border:5px solid var(--white)}
.about p{font:400 13px/19px "Josefin Sans",sans-serif;margin-top:50px}
.btn-outline{display:inline-block;margin-top:20px;border:1.5px solid var(--white);color:var(--white);font:600 11px/30px "Open Sans",sans-serif;padding:0 18px}
.social-grid{display:grid;grid-template-columns:160px 160px;gap:6px 10px;margin-top:10px}
.tile{height:64px;color:var(--white);display:flex;align-items:center;gap:10px;padding:0 10px;font:400 11px/14px "Open Sans",sans-serif}
.tile i{width:22px;height:22px;border-radius:50%;background:rgba(255,255,255,.85);flex:none}
.tile b{display:block;font-weight:700}
.ad{height:280px;position:relative;margin:0 26px}
.ad .ph{position:absolute;left:0;top:0;width:140px;height:280px}
.ad-copy{position:absolute;right:0;top:22px;width:130px;text-align:center;color:#333}
.ad-copy small{font:400 13px/16px "Libre Baskerville",serif;letter-spacing:2px}
.ad-copy strong{display:block;font:700 21px/24px "Libre Baskerville",serif;margin-top:6px}
.ad-btn{display:inline-block;margin-top:120px;background:#4aa5a5;color:var(--white);font:600 12px/28px "Open Sans",sans-serif;padding:0 14px}
.box{background:var(--panel)}
.newsletter{height:224px;padding:16px 16px}
.newsletter p{font:400 13px/18px "Josefin Sans",sans-serif;color:#555}
.field{background:var(--white);border:1px solid #ddd;height:36px;margin-top:12px;font:400 12px/34px "Open Sans",sans-serif;color:#777;padding-left:10px}
.btn-sub{height:36px;margin-top:14px;background:var(--red);color:var(--white);text-align:center;font:700 13px/36px "Open Sans",sans-serif}
.updates{height:253px;text-align:center;padding:22px 30px}
.update-dot{width:36px;height:36px;border-radius:50%;background:var(--tw);margin:0 auto}
.updates p{font:400 14px/20px "Josefin Sans",sans-serif;color:#444;margin-top:16px}
.updates a{color:var(--cyan);text-decoration:none}
.updates .date{font:400 10px/16px "Open Sans",sans-serif;color:var(--muted);margin-top:4px}
.update-act{font:400 12px/18px "Josefin Sans",sans-serif;color:var(--cyan);margin-top:6px}
.dots{display:flex;justify-content:center;gap:6px;margin-top:10px}
.dots i{width:7px;height:7px;border-radius:50%;background:#ccc}
.dots i:first-child{background:var(--cyan)}
.archive{height:218px;padding:12px 20px;list-style:none}
.archive li{font:400 14px/36px "Josefin Sans",sans-serif;color:#444;display:flex;align-items:center;gap:12px}
.archive li::before{content:"";width:8px;height:8px;border-radius:50%;background:var(--cyan)}
.gallery{height:447px;padding:19px 37px}
.gallery-grid{display:grid;grid-template-columns:repeat(3,80px);gap:4px}
.gallery-grid .ph{height:80px}
.btn-gallery{display:block;margin:32px auto 0;width:260px;background:var(--white);border:1px solid #999;text-align:center;font:400 12px/36px "Open Sans",sans-serif;color:#444}

/* footer */
.footer{left:0;top:3804px;width:1200px;height:187px;background:var(--dark);text-align:center}
.foot-nav{margin-top:36px;font:400 13px/20px "Josefin Sans",sans-serif;color:#ccc;text-transform:uppercase}
.foot-nav span{margin:0 10px;color:#777}
.foot-icons{display:flex;justify-content:center;gap:6px;margin-top:28px}
.foot-icons .ico{border-color:#bbb;width:28px;height:28px}
.copy{margin-top:34px;font:400 12px/16px "Josefin Sans",sans-serif;color:#999}
</style>
</head>
<body>

<header class="abs topbar">
  <div class="abs logo">BrightNomadRx</div>
  <div class="abs social-top">
    <i class="ico"></i><i class="ico"></i><i class="ico"></i><i class="ico"></i><i class="ico"></i><i class="ico"></i><i class="ico"></i>
  </div>
</header>
<nav class="abs navbar">
  <div class="abs nav">
    <a class="active">Home</a><a>About Us</a><a>Travel</a><a>Lifestyle</a><a>Life Hacking</a><a>Medicine</a><a>Contact</a>
  </div>
  <div class="abs search">Search
    <svg width="14" height="14" viewBox="0 0 14 14"><circle cx="6" cy="6" r="4.5" fill="none" stroke="#ddd" stroke-width="1.6"/><line x1="9.3" y1="9.3" x2="13" y2="13" stroke="#ddd" stroke-width="1.8"/></svg>
  </div>
</nav>

<section class="abs hero ph" role="img" aria-label="Woman in a sun hat sitting under a tree beside a bicycle at sunset"></section>
<div class="abs hero-tag">LIFE STYLE</div>
<h1 class="abs hero-title">Lorem ipsum dolor sit amet, consectetur adipiscing elit, sed do eiusmod tempor incididunt ut labore et dolore magna aliqua.</h1>

<!-- Travel -->
<div class="abs col-main sec-head" style="top:686px"><span class="tab">Travel</span><span class="more">MORE</span></div>
<div class="abs col-main" style="top:737px;display:flex;gap:14px">
  <div class="feature" style="width:344px">
    <div class="ph ph-sea" role="img" aria-label="Traveller with arms raised on a seaside cliff"></div>
    <div class="shade"></div>
    <div class="cap"><span class="badge">Featured</span><h3>Lorem ipsum dolor sit amet, consectetur adipiscing elit.</h3><div class="meta"><span>John Smith</span><span>18 Comments</span></div></div>
  </div>
  <div style="width:350px">
    <div class="mini"><div class="ph ph-beach" role="img" aria-label="Tropical beach"></div><div><h4>Lorem ipsum dolor sit amet, consectetur adipiscing elit.</h4><div class="meta"><span>18/10/2016</span><span>18 Comments</span></div></div></div>
    <div class="mini"><div class="ph ph-boat" role="img" aria-label="Longtail boat on clear water"></div><div><h4>Lorem ipsum dolor sit amet, consectetur adipiscing elit.</h4><div class="meta"><span>18/10/2016</span><span>18 Comments</span></div></div></div>
    <div class="mini"><div class="ph ph-girl" role="img" aria-label="Woman in a sun hat outdoors"></div><div><h4>Lorem ipsum dolor sit amet, consectetur adipiscing elit.</h4><div class="meta"><span>18/10/2016</span><span>18 Comments</span></div></div></div>
  </div>
</div>

<!-- Life style / Medicine -->
<div class="abs col-main two" style="top:1059px">
  <div class="sec-head red"><span class="tab">Life Style</span><span class="more">MORE</span></div>
  <div class="sec-head orange"><span class="tab">Medicine</span><span class="more">MORE</span></div>
</div>
<div class="abs col-main two" style="top:1109px">
  <div>
    <div class="feature"><div class="ph ph-people" role="img" aria-label="Friends laughing outdoors"></div><div class="shade"></div>
      <div class="cap"><span class="badge">Featured</span><h3>Lorem ipsum dolor sit amet, consectetur adipiscing elit.</h3><div class="meta"><span>John Smith</span><span>18 Comments</span></div></div></div>
    <div style="margin-top:14px">
      <div class="mini"><div class="ph ph-people" role="img" aria-label="Group of friends"></div><div><h4>Lorem ipsum dolor sit amet, consectetur adipiscing elit.</h4><div class="meta"><span>18/10/2016</span><span>18 Comments</span></div></div></div>
      <div class="mini"><div class="ph ph-people" role="img" aria-label="Couple smiling"></div><div><h4>Lorem ipsum dolor sit amet, consectetur adipiscing elit.</h4><div class="meta"><span>18/10/2016</span><span>18 Comments</span></div></div></div>
      <div class="mini"><div class="ph ph-car" role="img" aria-label="Road trip in a car"></div><div><h4>Lorem ipsum dolor sit amet, consectetur adipiscing elit.</h4><div class="meta"><span>18/10/2016</span><span>18 Comments</span></div></div></div>
    </div>
  </div>
  <div>
    <div class="feature"><div class="ph ph-pills" role="img" aria-label="Pills and capsules on a table"></div><div class="shade"></div>
      <div class="cap"><span class="badge">Featured</span><h3>Lorem ipsum dolor sit amet, consectetur adipiscing elit.</h3><div class="meta"><span>John Smith</span><span>18 Comments</span></div></div></div>
    <div style="margin-top:14px">
      <div class="mini"><div class="ph ph-pills" role="img" aria-label="Medical capsules"></div><div><h4>Lorem ipsum dolor sit amet, consectetur adipiscing elit.</h4><div class="meta"><span>18/10/2016</span><span>18 Comments</span></div></div></div>
      <div class="mini"><div class="ph ph-food" role="img" aria-label="Fresh salad bowl"></div><div><h4>Lorem ipsum dolor sit amet, consectetur adipiscing elit.</h4><div class="meta"><span>18/10/2016</span><span>18 Comments</span></div></div></div>
      <div class="mini"><div class="ph ph-doctor" role="img" aria-label="Doctor in a clinic"></div><div><h4>Lorem ipsum dolor sit amet, consectetur adipiscing elit.</h4><div class="meta"><span>18/10/2016</span><span>18 Comments</span></div></div></div>
    </div>
  </div>
</div>

<!-- Recent posts -->
<div class="abs col-main sec-head" style="top:1742px"><span class="tab">Recent Posts</span><span class="more">MORE</span></div>
<div class="abs col-main" style="top:1793px">
  <article class="post"><div class="thumb"><div class="ph ph-beach" role="img" aria-label="Woman relaxing by the sea"></div><span class="cat" style="background:var(--cyan)">Travel</span></div>
    <div><h4>Lorem ipsum dolor sit amet, consectetur adipiscing elit,</h4><div class="meta"><span>John Smith</span><span>18/10/2016</span><span>18 Comments</span></div><p>Lorem ipsum dolor sit amet, consectetur adipiscing elit, sed do eiusmod tempor incididunt ut labore et dolore magna aliqua.</p><span class="btn-read">READ MORE</span></div></article>
  <article class="post"><div class="thumb"><div class="ph ph-bike" role="img" aria-label="Woman riding a bicycle"></div><span class="cat" style="background:var(--red)">Lifestyle</span></div>
    <div><h4>Lorem ipsum dolor sit amet, consectetur adipiscing elit,</h4><div class="meta"><span>John Smith</span><span>18/10/2016</span><span>18 Comments</span></div><p>Lorem ipsum dolor sit amet, consectetur adipiscing elit, sed do eiusmod tempor incididunt ut labore et dolore magna aliqua.</p><span class="btn-read">READ MORE</span></div></article>
  <article class="post"><div class="thumb"><div class="ph ph-laptop" role="img" aria-label="Glowing laptop in a dark room"></div><span class="cat" style="background:var(--green)">Life Hacking</span></div>
    <div><h4>Lorem ipsum dolor sit amet, consectetur adipiscing elit,</h4><div class="meta"><span>John Smith</span><span>18/10/2016</span><span>18 Comments</span></div><p>Lorem ipsum dolor sit amet, consectetur adipiscing elit, sed do eiusmod tempor incididunt ut labore et dolore magna aliqua.</p><span class="btn-read">READ MORE</span></div></article>
  <article class="post"><div class="thumb"><div class="ph ph-doctor" role="img" aria-label="Doctor with a stethoscope"></div><span class="cat" style="background:var(--orange)">Medicine</span></div>
    <div><h4>Lorem ipsum dolor sit amet, consectetur adipiscing elit,</h4><div class="meta"><span>John Smith</span><span>18/10/2016</span><span>18 Comments</span></div><p>Lorem ipsum dolor sit amet, consectetur adipiscing elit, sed do eiusmod tempor incididunt ut labore et dolore magna aliqua.</p><span class="btn-read">READ MORE</span></div></article>
  <article class="post"><div class="thumb"><div class="ph ph-girl" role="img" aria-label="Woman in a hat in a sunny field"></div><span class="cat" style="background:var(--cyan)">Travel</span></div>
    <div><h4>Lorem ipsum dolor sit amet, consectetur adipiscing elit,</h4><div class="meta"><span>John Smith</span><span>18/10/2016</span><span>18 Comments</span></div><p>Lorem ipsum dolor sit amet, consectetur adipiscing elit, sed do eiusmod tempor incididunt ut labore et dolore magna aliqua.</p><span class="btn-read">READ MORE</span></div></article>
</div>
<div class="abs col-main pager" style="top:2672px">‹&nbsp; NEWER POSTS<span>/</span>OLDER POSTS &nbsp;›</div>

<!-- Travel (repeat) -->
<div class="abs col-main sec-head" style="top:2719px"><span class="tab">Travel</span><span class="more">MORE</span></div>
<div class="abs col-main" style="top:2766px;display:flex;gap:14px">
  <div class="feature" style="width:344px">
    <div class="ph ph-sea" role="img" aria-label="Traveller with arms raised on a seaside cliff"></div>
    <div class="shade"></div>
    <div class="cap"><span class="badge">Featured</span><h3>Lorem ipsum dolor sit amet, consectetur adipiscing elit.</h3><div class="meta"><span>John Smith</span><span>18 Comments</span></div></div>
  </div>
  <div style="width:350px">
    <div class="mini"><div class="ph ph-beach" role="img" aria-label="Tropical beach"></div><div><h4>Lorem ipsum dolor sit amet, consectetur adipiscing elit.</h4><div class="meta"><span>18/10/2016</span><span>18 Comments</span></div></div></div>
    <div class="mini"><div class="ph ph-boat" role="img" aria-label="Longtail boat on clear water"></div><div><h4>Lorem ipsum dolor sit amet, consectetur adipiscing elit.</h4><div class="meta"><span>18/10/2016</span><span>18 Comments</span></div></div></div>
    <div class="mini"><div class="ph ph-girl" role="img" aria-label="Woman in a sun hat outdoors"></div><div><h4>Lorem ipsum dolor sit amet, consectetur adipiscing elit.</h4><div class="meta"><span>18/10/2016</span><span>18 Comments</span></div></div></div>
  </div>
</div>

<!-- Life style / Medicine (repeat) -->
<div class="abs col-main two" style="top:3094px">
  <div class="sec-head red"><span class="tab">Life Style</span><span class="more">MORE</span></div>
  <div class="sec-head orange"><span class="tab">Medicine</span><span class="more">MORE</span></div>
</div>
<div class="abs col-main two" style="top:3144px">
  <div>
    <div class="feature"><div class="ph ph-people" role="img" aria-label="Friends laughing outdoors"></div><div class="shade"></div>
      <div class="cap"><span class="badge">Featured</span><h3>Lorem ipsum dolor sit amet, consectetur adipiscing elit.</h3><div class="meta"><span>John Smith</span><span>18 Comments</span></div></div></div>
    <div style="margin-top:14px">
      <div class="mini"><div class="ph ph-people" role="img" aria-label="Group of friends"></div><div><h4>Lorem ipsum dolor sit amet, consectetur adipiscing elit.</h4><div class="meta"><span>18/10/2016</span><span>18 Comments</span></div></div></div>
      <div class="mini"><div class="ph ph-people" role="img" aria-label="Couple smiling"></div><div><h4>Lorem ipsum dolor sit amet, consectetur adipiscing elit.</h4><div class="meta"><span>18/10/2016</span><span>18 Comments</span></div></div></div>
      <div class="mini"><div class="ph ph-car" role="img" aria-label="Road trip in a car"></div><div><h4>Lorem ipsum dolor sit amet, consectetur adipiscing elit.</h4><div class="meta"><span>18/10/2016</span><span>18 Comments</span></div></div></div>
    </div>
  </div>
  <div>
    <div class="feature"><div class="ph ph-pills" role="img" aria-label="Pills and capsules on a table"></div><div class="shade"></div>
      <div class="cap"><span class="badge">Featured</span><h3>Lorem ipsum dolor sit amet, consectetur adipiscing elit.</h3><div class="meta"><span>John Smith</span><span>18 Comments</span></div></div></div>
    <div style="margin-top:14px">
      <div class="mini"><div class="ph ph-pills" role="img" aria-label="Medical capsules"></div><div><h4>Lorem ipsum dolor sit amet, consectetur adipiscing elit.</h4><div class="meta"><span>18/10/2016</span><span>18 Comments</span></div></div></div>
      <div class="mini"><div class="ph ph-food" role="img" aria-label="Fresh salad bowl"></div><div><h4>Lorem ipsum dolor sit amet, consectetur adipiscing elit.</h4><div class="meta"><span>18/10/2016</span><span>18 Comments</span></div></div></div>
      <div class="mini"><div class="ph ph-doctor" role="img" aria-label="Doctor in a clinic"></div><div><h4>Lorem ipsum dolor sit amet, consectetur adipiscing elit.</h4><div class="meta"><span>18/10/2016</span><span>18 Comments</span></div></div></div>
    </div>
  </div>
</div>

<!-- Sidebar -->
<div class="abs col-side sec-head" style="top:686px"><span class="tab">About Us</span></div>
<div class="abs col-side about" style="top:718px">
  <div class="avatar" role="img" aria-label="Portrait of the blog author"></div>
  <p>Lorem ipsum dolor sit amet, consectetur adipiscing elit, sed do eiusmod tempor incididunt ut labore et dolore magna aliqua. Ut enim ad minim veniam, quis nostrud exercitation ullamco laboris nisi ut aliquip ex ea commodo consequat. Duis aute irure dolor in reprehenderit.</p>
  <span class="btn-outline">READ MORE</span>
</div>

<div class="abs col-side sec-head" style="top:1165px"><span class="tab">Keep In Touch</span></div>
<div class="abs col-side social-grid" style="top:1198px">
  <div class="tile" style="background:var(--fb)"><i></i><span><b>1200</b>FANS</span></div>
  <div class="tile" style="background:var(--tw)"><i></i><span><b>14</b>FOLLOWERS</span></div>
  <div class="tile" style="background:var(--yt)"><i></i><span><b>4500</b>SUBSCRIBERS</span></div>
  <div class="tile" style="background:var(--vm)"><i></i><span><b>1</b>SUBSCRIBERS</span></div>
  <div class="tile" style="background:var(--dr)"><i></i><span><b>100</b>FOLLOWERS</span></div>
  <div class="tile" style="background:var(--rss)"><i></i><span><b>SUBSCRIBE</b>TO RSS FEED</span></div>
</div>

<div class="abs col-side" style="top:1444px">
  <div class="ad">
    <div class="ph ph-watch" role="img" aria-label="Wooden wristwatch with a red dial"></div>
    <div class="ad-copy"><small>LUXURY</small><strong>WOOD WATCHES</strong><span class="ad-btn">SHOP NOW</span></div>
  </div>
</div>

<div class="abs col-side sec-head" style="top:1756px"><span class="tab">Newsletter!</span></div>
<div class="abs col-side box newsletter" style="top:1790px">
  <p>Subscribe my Newsletter for new recipes, right from your inbox. Let's stay updated!</p>
  <div class="field">Name</div>
  <div class="field">Email</div>
  <div class="btn-sub">SUBSCRIBE NOW</div>
</div>

<div class="abs col-side sec-head" style="top:2043px"><span class="tab">Updates</span></div>
<div class="abs col-side box updates" style="top:2075px">
  <div class="update-dot"></div>
  <p>#Blog and #Magazine with 900+ #Demo #Homepages. Get it now: <a>brightnomadrx.com/demo</a></p>
  <div class="date">September 1, 2016</div>
  <div class="update-act">Reply &nbsp;|&nbsp; Repost &nbsp;|&nbsp; Favorite</div>
  <div class="dots"><i></i><i></i><i></i><i></i><i></i></div>
</div>

<div class="abs col-side sec-head" style="top:2360px"><span class="tab">Archive</span></div>
<ul class="abs col-side box archive" style="top:2392px">
  <li>May 2016</li><li>April 2015</li><li>January 2014</li><li>April 2014</li><li>March 2014</li><li>February 2014</li>
</ul>

<div class="abs col-side sec-head" style="top:2655px"><span class="tab">SnapRoll</span></div>
<div class="abs col-side box gallery" style="top:2687px">
  <div class="gallery-grid">
    <div class="ph ph-beach" role="img" aria-label="Beach photo"></div>
    <div class="ph ph-laptop" role="img" aria-label="Night scene photo"></div>
    <div class="ph ph-food" role="img" aria-label="Food photo"></div>
    <div class="ph ph-people" role="img" aria-label="Friends photo"></div>
    <div class="ph ph-sea" role="img" aria-label="Sea view photo"></div>
    <div class="ph ph-girl" role="img" aria-label="Outdoor portrait photo"></div>
    <div class="ph ph-car" role="img" aria-label="Road trip photo"></div>
    <div class="ph ph-boat" role="img" aria-label="Boat photo"></div>
    <div class="ph ph-people" role="img" aria-label="Group photo"></div>
    <div class="ph ph-bike" role="img" aria-label="Cycling photo"></div>
    <div class="ph ph-pills" role="img" aria-label="Still life photo"></div>
    <div class="ph ph-beach" role="img" aria-label="Holiday photo"></div>
  </div>
  <span class="btn-gallery">Follow Us On SnapRoll</span>
</div>

<!-- Footer -->
<footer class="abs footer">
  <div class="foot-nav">Home<span>/</span>About Us<span>/</span>Travel<span>/</span>Lifestyle<span>/</span>Life Hacking<span>/</span>Medicine<span>/</span>Contact</div>
  <div class="foot-icons"><i class="ico"></i><i class="ico"></i><i class="ico"></i><i class="ico"></i><i class="ico"></i><i class="ico"></i><i class="ico"></i></div>
  <div class="copy">Copyright ©2016 All Rights Reserved. Terms of Use | Privacy Policy</div>
</footer>

</body>
</html>
```